Tarrow Consulting Needs Standardised Stationery!

Hello,I am looking at having some standardised stationery to continue building my brand. I am looking for a relatively clean and simple designs using the colours from my logos. Tarrow Consulting is the main business with Career Beacon Australia a subsidiary.
In particular I am after a design for:
- Letterhead (very important), white background, professional, corporate that I can send to prospective clients. Logo colours.
- Envelope, standard design I can print onto envelopes.
- Pens
- Other stationery/promotional items I can create

Target Market(s)

Universities, government, large organisations.

Industry/Entity Type

Professional Service

Font styles to use
Serif

Requirements
Must have
• Logo, match the design of the Tarrow Consulting logo. Black Career Beacon Australia logo is a subsidiary.
Should not have
• Too much colour, some colour is good, but I am looking for a clean professional look.

```html
<!DOCTYPE html>
<html lang="en">
<head>
<meta charset="utf-8">
<title>Tarrow Consulting Letterhead</title>
<link href="https://fonts.googleapis.com/css2?family=Source+Sans+3:wght@400;600&family=Arimo:wght@700&display=swap" rel="stylesheet">
<style>
  :root {
    --backdrop: #e8e8e8;
    --paper: #f5f5f5;
    --ink: #3c3c3c;
    --ink-dark: #1f1f1f;
    --brand-blue: #0d93cf;
    --brand-orange: #e5833a;
    --white: #ffffff;
  }
  * { margin: 0; padding: 0; box-sizing: border-box; }
  html, body {
    width: 1200px; height: 1200px; overflow: hidden;
    background: var(--backdrop);
    font-family: "Source Sans 3", "Myriad Pro", sans-serif;
    color: var(--ink);
  }
  .letterhead {
    position: absolute; left: 189px; top: 20px;
    width: 822px; height: 1160px;
    background: var(--paper);
    box-shadow: 0 6px 24px rgba(0,0,0,0.12);
  }
  .brand {
    position: absolute; left: 62px; top: 52px;
    display: flex; align-items: center; gap: 12px;
  }
  .brand-square { width: 40px; height: 40px; background: var(--ink-dark); }
  .brand-name {
    font-size: 24px; font-weight: 600; letter-spacing: 1px;
    color: var(--ink-dark); text-transform: uppercase; line-height: 1;
  }
  .contact {
    position: absolute; right: 53px; top: 39px;
    text-align: right; font-size: 11.5px; line-height: 15.5px; color: var(--ink-dark);
  }
  .contact .gap { margin-top: 6px; }
  .contact-icon { display: inline-block; vertical-align: -2px; margin-left: 4px; }
  .greeting {
    position: absolute; left: 60px; top: 217px;
    font-family: "Arimo", Arial, sans-serif; font-weight: 700;
    font-size: 18px; color: var(--ink-dark);
  }
  .letter-body {
    position: absolute; left: 60px; right: 60px; top: 262px;
    font-size: 17px; line-height: 21.6px; text-align: justify;
  }
  .letter-body p { margin-bottom: 21.6px; }
  .signature {
    position: absolute; left: 60px; top: 823px;
    width: 133px; height: 67px;
    background: linear-gradient(180deg, #ececec, #e2e2e2);
  }
  .subsidiary {
    position: absolute; right: 55px; top: 1088px;
    display: flex; align-items: center; gap: 8px;
  }
  .subsidiary-circle { width: 36px; height: 36px; border-radius: 50%; background: var(--ink-dark); }
  .subsidiary-name {
    font-size: 17px; font-weight: 600; color: var(--ink-dark); line-height: 1.1;
  }
  .footer-bands { position: absolute; left: 0; bottom: 0; width: 822px; height: 24px; }
  .footer-url {
    position: absolute; right: 60px; bottom: 4px;
    font-size: 12px; letter-spacing: 0.6px; color: var(--white);
  }
</style>
</head>
<body>
  <div class="letterhead">
    <div class="brand">
      <span class="brand-square"></span>
      <span class="brand-name">Tarrow Consulting</span>
    </div>

    <div class="contact">
      <div>Po. box 201, Street Name,</div>
      <div>City Name, Zip Code - 00000</div>
      <div class="gap">0700 555 0142
        <svg class="contact-icon" width="9" height="10" viewBox="0 0 9 10"><path d="M2 2 Q7 1 7 6 L7 8 M5 6 L7 8.5 L9 6" fill="none" stroke="var(--brand-blue)" stroke-width="1.6"/></svg>
      </div>
      <div>info@tarrowconsulting.com
        <svg class="contact-icon" width="10" height="9" viewBox="0 0 10 9"><rect x="0.8" y="1.5" width="8.4" height="6" rx="1.5" fill="none" stroke="var(--brand-blue)" stroke-width="1.4"/><path d="M1 2 L5 5 L9 2" fill="none" stroke="var(--brand-blue)" stroke-width="1.2"/></svg>
      </div>
    </div>

    <div class="greeting">Dear Mr. Alder,</div>

    <div class="letter-body">
      <p>Lorem Ipsum is simply dummy text of the printing and typesetting industry. Lorem Ipsum has been the industry's standard dummy text ever since the 1500s, when an unknown printer took a galley of type and scrambled it to make a type specimen book. It has survived not only five centuries, but also the leap into electronic typesetting, remaining essentially unchanged.</p>
      <p>The standard chunk of Lorem Ipsum used since the 1500s is reproduced below for those interested. Sections 1.10.32 and 1.10.33 from "de Finibus Bonorum et Malorum" by Varelius are also reproduced in their exact original form, accompanied by English versions from the 1914 translation by H. Penwick</p>
      <p>Lorem Ipsum is simply dummy text of the printing and typesetting industry. Lorem Ipsum has been the industry's standard dummy text ever since the 1500s, when an unknown printer took a galley of type and scrambled it to make a type specimen book. It has survived not only five centuries, but also the leap into electronic typesetting, remaining essentially unchanged. It was popularised in the</p>
      <p>The standard chunk of Lorem Ipsum used since the 1500s is reproduced below for those interested. Sections 1.10.32 and 1.10.33 from "de Finibus Bonorum et Malorum" by Varelius are also reproduced in their exact original form, accompanied by English versions from the 1914 translation by H. Penwick</p>
      <p>The standard chunk of Lorem Ipsum used since the 1500s is reproduced below for those interested. Sections 1.10.32 and 1.10.33 from "de Finibus Bonorum et Malorum" by Varelius are also reproduced in their exact original form.</p>
    </div>

    <div class="signature" role="img" aria-label="Handwritten signature of the sender"></div>

    <div class="subsidiary">
      <span class="subsidiary-circle"></span>
      <span class="subsidiary-name">Career Beacon Australia</span>
    </div>

    <svg class="footer-bands" viewBox="0 0 822 24" preserveAspectRatio="none">
      <polygon points="0,0 577,0 571,9 0,9" fill="var(--brand-orange)"/>
      <polygon points="0,12 569,12 577,0 822,0 822,24 0,24" fill="var(--brand-blue)"/>
    </svg>
    <div class="footer-url">www.tarrowconsulting.com</div>
  </div>
</body>
</html>
```